Meridian Handsets business card design

I would like to see some designs for a business card for Meridian Handsets. I would like the business card to be double sided. It will need to have a similar colour / look and feel to our website www.meridianhandsets.com.au I have also attached our latest flyer. Final designs to be handed over in Photoshop format so that I can edit the business card when needed please.

Industry/Entity Type

Business

Contact Information for Business Card

Gavin Thornley
sales@meridianhandsets.com.au
Business Development Manager
ph: (08) 6197 5821
www.meridianhandsets.com.au

Font styles to use
Serif
Sans Serif

Requirements
Must have
• If you could please utilise our colour scheme as seen on our website and the attached flyer.
• I would also like the final design to be in a Photoshop format so that I can edit it when needed please.

```html
<!DOCTYPE html>
<html lang="en">
<head>
<meta charset="utf-8">
<title>Meridian Handsets – Business Card</title>
<link rel="stylesheet" href="https://fonts.googleapis.com/css2?family=Lato:wght@300;400;700&display=swap">
<style>
  :root {
    --page-bg: #e4e4e4;
    --card-white: #fbfbfb;
    --brand-blue: #1f78c4;
    --brand-teal: #3dbf98;
    --ink-dark: #1e1f24;
    --ink-mid: #3a3b40;
    --band-dark: #333436;
    --icon-blue: #2a6fb8;
    --text-white: #ffffff;
  }
  * { box-sizing: border-box; margin: 0; padding: 0; }
  html, body {
    width: 1200px; height: 960px; overflow: hidden;
    background: var(--page-bg);
    font-family: "Lato", Arial, sans-serif;
  }
  .canvas {
    width: 1200px; height: 960px;
    display: flex; flex-direction: column;
    align-items: center; justify-content: center; gap: 56px;
  }
  .card {
    position: relative;
    width: 660px; height: 400px;
    background: var(--card-white);
    box-shadow: 0 6px 18px rgba(0,0,0,0.18);
    overflow: hidden;
  }

  /* Back side */
  .card-back { padding: 22px; }
  .back-panel {
    width: 100%; height: 100%;
    background: linear-gradient(200deg, var(--brand-teal) 0%, #2a98b6 35%, var(--brand-blue) 70%);
    display: flex; flex-direction: column; align-items: center; justify-content: center;
  }
  .back-name {
    font-weight: 700; font-size: 50px; color: var(--ink-dark);
    letter-spacing: -0.5px;
  }
  .back-url {
    margin-top: 6px;
    font-weight: 400; font-size: 22px; color: var(--ink-dark);
    letter-spacing: 0.3px;
  }

  /* Front side */
  .front-shapes { position: absolute; inset: 0; }
  .front-name-mark {
    position: absolute; left: 48px; top: 62px;
    font-weight: 700; font-size: 44px; color: var(--ink-dark);
    letter-spacing: -0.5px;
  }
  .person { position: absolute; left: 52px; top: 160px; }
  .person-name { font-weight: 700; font-size: 26px; color: var(--ink-dark); }
  .person-title { font-weight: 300; font-size: 19px; color: var(--ink-mid); margin-top: 2px; }
  .contact-list {
    position: absolute; left: 52px; top: 238px;
    list-style: none;
  }
  .contact-list li {
    display: flex; align-items: center; gap: 10px;
    font-weight: 300; font-size: 18px; color: var(--ink-mid);
    height: 30px;
  }
  .contact-icon { width: 18px; height: 18px; flex: none; }
  .band-url {
    position: absolute; left: 52px; top: 352px;
    display: flex; align-items: center; gap: 12px;
    font-weight: 400; font-size: 19px; color: var(--text-white);
    letter-spacing: 0.3px;
  }
</style>
</head>
<body>
<main class="canvas">

  <section class="card card-back" aria-label="Card back">
    <div class="back-panel">
      <p class="back-name">Meridian Handsets</p>
      <p class="back-url">www.meridianhandsets.com.au</p>
    </div>
  </section>

  <section class="card card-front" aria-label="Card front">
    <svg class="front-shapes" viewBox="0 0 660 400" width="660" height="400" aria-hidden="true">
      <defs>
        <linearGradient id="tab-gradient" x1="0" y1="0" x2="0" y2="1">
          <stop offset="0" stop-color="#1f78c4"/>
          <stop offset="1" stop-color="#3dbf98"/>
        </linearGradient>
      </defs>
      <path class="accent-tab" d="M470 300 L470 130 Q470 80 520 80 L660 80 L660 300 Z" fill="url(#tab-gradient)"/>
      <path class="accent-line" d="M0 314 L440 314 L440 322 L0 322 Z" fill="#1f78c4"/>
      <path class="footer-band" d="M0 322 L440 322 L480 284 L660 284 L660 400 L0 400 Z" fill="#333436"/>
    </svg>

    <p class="front-name-mark">Meridian Handsets</p>

    <div class="person">
      <p class="person-name">Gavin Thornley</p>
      <p class="person-title">Business Development Manager</p>
    </div>

    <ul class="contact-list">
      <li>
        <svg class="contact-icon" viewBox="0 0 20 20" aria-hidden="true">
          <circle cx="10" cy="10" r="9" fill="none" stroke="#2a6fb8" stroke-width="1.6"/>
          <path d="M7 5.5 L8.6 5.5 L9.2 8 L8.2 8.8 Q9 11 11.2 11.8 L12 10.8 L14.5 11.4 L14.5 13 Q13.5 14.5 11.5 14 Q6.5 12.5 6 7.5 Q6 6 7 5.5 Z" fill="#2a6fb8"/>
        </svg>
        <span>+ (08) 6197 5821</span>
      </li>
      <li>
        <svg class="contact-icon" viewBox="0 0 20 20" aria-hidden="true">
          <rect x="2" y="5" width="16" height="11" rx="1.5" fill="#2a6fb8"/>
          <path d="M2.5 5.5 L10 11 L17.5 5.5" fill="none" stroke="#ffffff" stroke-width="1.4"/>
        </svg>
        <span>sales@meridianhandsets.com.au</span>
      </li>
    </ul>

    <p class="band-url">
      <svg class="contact-icon" viewBox="0 0 20 20" aria-hidden="true">
        <rect x="2" y="3.5" width="16" height="10.5" rx="1" fill="none" stroke="#ffffff" stroke-width="1.6"/>
        <path d="M8 14 L7 17 L13 17 L12 14" fill="#ffffff"/>
      </svg>
      <span>www.meridianhandsets.com.au</span>
    </p>
  </section>

</main>
</body>
</html>
```